White Cane Law Awareness Poster

Steady Harbor is a disability advocacy organization in Indiana. We are working on a project with the Hollow Creek Council of Vision Allies. Our organizations need a design for a poster to promote awareness of Indiana's White Cane law. This poster will be displayed in local libraries, businesses, and other public places.

The poster should catch people's attention, and briefly explain that drivers have to yield for pedestrians who are blind who have white canes or seeing eye dogs.

The poster should be designed with people with low vision in mind. This means large text in a clear font, with good contrast between the text and the background. The text should be in a sans serif font that is clear and easy to read, with no italics or script fonts. There should not be a "busy" picture or pattern behind the text.

The poster should also include a reference to the relevant laws. We have attached a document with those references.

Finally, the poster should include the logos of Steady Harbor and the Hollow Creek Council of Vision Allies, which we have included as attachments.

We have also included an attachment with a photo of the old White Cane Law poster, just to show an example of what we DO NOT want.

Industry/Entity Type

Non-Profit

Font styles to use
Sans Serif

Requirements
Must have
• The poster should also include a reference to the relevant laws. We have attached a document with those references.
• Finally, the poster should include the logos of Steady Harbor and the Hollow Creek Council of Vision Allies, which we have included as attachments.

```html
<!DOCTYPE html>
<html lang="en">
<head>
<meta charset="utf-8">
<title>White Cane Law Awareness Poster</title>
<link rel="stylesheet" href="https://fonts.googleapis.com/css2?family=Fira+Sans+Condensed:wght@500;600&family=Open+Sans:wght@700;800&display=swap">
<style>
  :root {
    --page: #e8e4de;
    --paper: #ffffff;
    --ink: #111111;
    --alert-red: #e4202a;
    --signal-blue: #1f4fe8;
    --white: #ffffff;
  }
  html, body {
    margin: 0;
    width: 1200px;
    height: 1200px;
    overflow: hidden;
    background: var(--page);
  }
  .poster {
    position: absolute;
    left: 220px;
    top: 25px;
    width: 760px;
    height: 1150px;
    background: var(--paper);
    font-family: "Open Sans", Arial, sans-serif;
    color: var(--ink);
  }
  .header-shape {
    position: absolute;
    left: 0;
    top: 0;
  }
  .headline {
    position: absolute;
    top: 0;
    left: 0;
    width: 760px;
    height: 123px;
    margin: 0;
    display: flex;
    align-items: center;
    justify-content: center;
    color: var(--white);
    font-size: 86px;
    font-weight: 800;
    letter-spacing: 1px;
  }
  .scene-art {
    position: absolute;
    left: 194px;
    top: 145px;
    width: 376px;
    height: 232px;
    background: linear-gradient(90deg, var(--signal-blue) 0%, var(--signal-blue) 55%, #1a1a1a 70%, var(--ink) 100%);
  }
  .law-title {
    position: absolute;
    top: 400px;
    left: 0;
    width: 760px;
    margin: 0;
    text-align: center;
    color: var(--alert-red);
    font-size: 72px;
    font-weight: 800;
    line-height: 1;
    letter-spacing: 1px;
  }
  .law-summary {
    position: absolute;
    top: 478px;
    left: 0;
    width: 760px;
    margin: 0;
    text-align: center;
    font-size: 38px;
    font-weight: 700;
    line-height: 46px;
  }
  .partners {
    position: absolute;
    top: 700px;
    left: 0;
    width: 760px;
    height: 130px;
  }
  .partner {
    position: absolute;
    top: 0;
    height: 130px;
    display: flex;
    flex-direction: column;
    align-items: center;
    justify-content: center;
    text-align: center;
    font-family: "Open Sans", Arial, sans-serif;
    font-weight: 700;
  }
  .partner-council {
    left: 110px;
    width: 320px;
    color: var(--ink);
    font-size: 22px;
    line-height: 1.2;
  }
  .partner-council .mark {
    width: 30px;
    height: 30px;
    border-radius: 50%;
    background: var(--ink);
    margin-bottom: 8px;
  }
  .partner-council .chapter {
    margin-top: 6px;
    font-size: 20px;
  }
  .partner-harbor {
    left: 440px;
    width: 220px;
    color: var(--signal-blue);
    font-size: 30px;
  }
  .partner-harbor .mark {
    width: 44px;
    height: 44px;
    border-radius: 50%;
    background: var(--signal-blue);
    margin-bottom: 10px;
  }
  .call-band {
    position: absolute;
    top: 836px;
    left: 0;
    width: 760px;
    height: 86px;
    margin: 0;
    background: var(--signal-blue);
    color: var(--white);
    display: flex;
    align-items: center;
    justify-content: center;
    font-size: 46px;
    font-weight: 800;
    letter-spacing: 4px;
  }
  .statutes {
    position: absolute;
    top: 932px;
    left: 30px;
    width: 700px;
    text-align: center;
    font-family: "Fira Sans Condensed", "Arial Narrow", sans-serif;
    font-weight: 600;
    font-size: 15.5px;
    line-height: 22px;
    color: var(--ink);
  }
  .statute-heading {
    margin: 0;
    color: var(--alert-red);
    font-size: 21px;
    line-height: 28px;
    text-decoration: underline;
    text-underline-offset: 3px;
  }
  .statute-text {
    margin: 0 0 4px;
  }
</style>
</head>
<body>
  <article class="poster">
    <svg class="header-shape" width="760" height="215" viewBox="0 0 760 215" aria-hidden="true">
      <polygon points="0,0 78,0 0,212" fill="var(--alert-red)"/>
      <polygon points="682,0 760,0 760,212" fill="var(--alert-red)"/>
      <polygon points="78,0 682,0 727,123 33,123" fill="var(--ink)"/>
    </svg>
    <h1 class="headline">BE AWARE!</h1>

    <div class="scene-art" role="img" aria-label="Pictogram of a blue car stopping for a pedestrian with a white cane and a guide dog"></div>

    <h2 class="law-title">INDIANA LAW</h2>
    <p class="law-summary">Requires drivers<br>to yield for pedestrians<br>who are blind, who have white<br>canes or seeing eye dogs.</p>

    <div class="partners">
      <div class="partner partner-council">
        <span class="mark"></span>
        <span>Hollow Creek Council<br>of Vision Allies</span>
        <span class="chapter">Maple Ridge Chapter</span>
      </div>
      <div class="partner partner-harbor">
        <span class="mark"></span>
        <span>Steady Harbor</span>
      </div>
    </div>

    <p class="call-band">STOP AND SAVE LIFE!</p>

    <section class="statutes">
      <h3 class="statute-heading">INDIANA WHITE CANE LAW</h3>
      <p class="statute-text">Ind. Code § 9-21-17-21 : Indiana Code - Section 9-21-17-21: Blind pedestrians; yield of right-of-way<br>A person who drives a vehicle shall yield the right-of-way to a blind pedestrian carrying a clearly visible<br>white cane or accompanied by a guide dog.</p>
      <h3 class="statute-heading">PENALTY</h3>
      <p class="statute-text">Ind. Code § 9-21-17-24 : Indiana Code - Section 9-21-17-24: Violations; Class C infraction<br>A person who violates this chapter commits a Class C infraction. (Misdemeanor)</p>
    </section>
  </article>
</body>
</html>
```